Byte Wardens Inc. IT Services and Sales

We need a new business card design for our new company. We have a current logo but are open and encourage any redesigns.

Byte Wardens is derived in our history from computer gaming. (Nebulith References, STORM UNBROKEN!!!). We as a group have been together since high school (2002). Our friendships brought us together and now we are all business partners providing IT Support and Consultation Services ranging from fixing small issues like printers, home networking, pc building to custom application development and managed cloud and it networks for our clients.
We would like our design to communicate that we strive to be the best (we are born gamers and have a highly competitive instinct) and offer solutions to problems that other companies just simply say we can't do it. We are always looking to go above and beyond for our clients, learning our clients business and figuring out ways to help them make more money by optimizing the way they do business, offering solutions so they can grow their business and helping everyone utilize the technology they have or advise them with the technology they need to succeed.

Attached are things we have on our computers and logo's we have used.
One is a desktop background
while the other should be our logo.

Again, we are open to and encourage any logo redesigns in hope things can help with the direction we are looking into.

Please add a place for email as our current cards have no email and it makes us very sad.
Updates

Hi All,

Just wanted to say thank you for all those who submitted a design. We've updated our project to include the fact that we are open and encourage a logo redesign. Also, this project is now committed to payment.

Target Market(s)

We will be handing these out to all our future business prospects. Prospects are usually business owners that can be in any industry. They look to us to be cutting edge or professional.

Industry/Entity Type

High School

Requirements
Must have
• name, title, work, fax, and cell phone, address and email

```html
<!DOCTYPE html>
<html lang="en">
<head>
<meta charset="utf-8">
<title>Byte Wardens Inc. – Business Card</title>
<link rel="stylesheet" href="https://fonts.googleapis.com/css2?family=Open+Sans:wght@300;400;600&display=swap">
<style>
  :root {
    --stage: #2a2a2b;
    --card: #3a3a3c;
    --card-shadow: rgba(0, 0, 0, 0.45);
    --accent: #e05a2b;
    --sphere: #3ec3f0;
    --ink: #f2f2f2;
    --ink-soft: #c9c9c9;
  }
  html, body {
    margin: 0;
    padding: 0;
    width: 1200px;
    height: 1000px;
    overflow: hidden;
    background: var(--stage);
    font-family: "Open Sans", Arial, sans-serif;
  }
  .canvas {
    position: relative;
    width: 1200px;
    height: 1000px;
  }
  .card {
    position: absolute;
    top: 328px;
    height: 342px;
    background: var(--card);
    border-radius: 18px;
    box-shadow: 0 6px 14px var(--card-shadow);
  }
  .card-front { left: 65px; width: 525px; }
  .card-back  { left: 605px; width: 535px; }

  /* Front: brand name with a single disc */
  .front-brand {
    position: absolute;
    left: 0; right: 0;
    top: 146px;
    display: flex;
    align-items: center;
    justify-content: center;
    gap: 18px;
  }
  .brand-dot {
    width: 54px;
    height: 54px;
    border-radius: 50%;
    background: var(--sphere);
  }
  .brand-name {
    color: var(--ink);
    font-weight: 300;
    font-size: 40px;
    letter-spacing: 0.5px;
    line-height: 1;
  }

  /* Back: brand line */
  .back-brand {
    position: absolute;
    left: 24px;
    top: 146px;
    display: flex;
    align-items: center;
    gap: 10px;
  }
  .back-brand .brand-dot { width: 28px; height: 28px; }
  .back-brand .brand-name { font-size: 30px; }

  /* Back: person */
  .person {
    position: absolute;
    left: 335px;
    top: 47px;
  }
  .person-name {
    margin: 0;
    color: var(--accent);
    font-size: 15px;
    font-weight: 400;
    letter-spacing: 0.3px;
    text-transform: uppercase;
  }
  .person-title {
    margin: 1px 0 0;
    color: var(--ink-soft);
    font-size: 12.5px;
  }

  /* Back: contact list */
  .contact-list {
    position: absolute;
    left: 332px;
    top: 130px;
    margin: 0;
    padding: 0;
    list-style: none;
  }
  .contact-list li {
    display: flex;
    align-items: center;
    gap: 6px;
    height: 23px;
    color: var(--ink);
    font-size: 12.5px;
  }
  .contact-icon { width: 11px; height: 11px; fill: var(--accent); flex: none; }

  .address {
    position: absolute;
    left: 335px;
    top: 243px;
    margin: 0;
    color: var(--ink-soft);
    font-size: 12px;
    font-style: normal;
    line-height: 18px;
  }
</style>
</head>
<body>
<main class="canvas">

  <section class="card card-front" aria-label="Card front">
    <div class="front-brand">
      <span class="brand-dot"></span>
      <span class="brand-name">Byte Wardens</span>
    </div>
  </section>

  <section class="card card-back" aria-label="Card back">
    <div class="back-brand">
      <span class="brand-dot"></span>
      <span class="brand-name">Byte Wardens</span>
    </div>

    <div class="person">
      <h1 class="person-name">Marcus Vale</h1>
      <p class="person-title">Director of Operations</p>
    </div>

    <ul class="contact-list">
      <li>
        <svg class="contact-icon" viewBox="0 0 12 12" aria-hidden="true"><rect x="3" y="0" width="6" height="12" rx="1"/><rect x="4" y="1.5" width="4" height="6" fill="#3a3a3c"/></svg>
        (555) 214 7730
      </li>
      <li>
        <svg class="contact-icon" viewBox="0 0 12 12" aria-hidden="true"><path d="M2.5 0.5 L4.5 0.5 L5.5 3.5 L4 4.7 C4.8 6.5 5.8 7.6 7.4 8.2 L8.6 6.7 L11.5 7.6 L11.5 9.8 C11.5 10.8 10.6 11.6 9.6 11.5 C5 11 1 7 0.6 2.4 C0.5 1.4 1.4 0.5 2.5 0.5 Z"/></svg>
        (555) 214 7731
      </li>
      <li>
        <svg class="contact-icon" viewBox="0 0 12 12" aria-hidden="true"><rect x="3" y="0.5" width="6" height="4"/><rect x="0.5" y="4.5" width="11" height="5" rx="1"/><rect x="3" y="8" width="6" height="3.5"/></svg>
        (555) 214 7732
      </li>
      <li>
        <svg class="contact-icon" viewBox="0 0 12 12" aria-hidden="true"><rect x="0.5" y="2" width="11" height="8"/><path d="M0.5 2 L6 6.5 L11.5 2" fill="none" stroke="#3a3a3c" stroke-width="1.2"/></svg>
        yourname@bytewardens.com
      </li>
    </ul>

    <address class="address">
      4470 Larkspur Ave.,<br>
      Suite C, Fairhollow, CA. 95871
    </address>
  </section>

</main>
</body>
</html>
```